business card with 2 locations on 1 card

I need a modern looking business card that I would use at 2 different locations. Possibly 1 location on 1 side and other location on other side. One should be able to distinguish the 2 locations immediately before having to read the address or description on card. You can take a look at my website to see what I'm drawn to. The logo is brand new that I just purchased on Craft Hive. I want to emphasize family.
Updates

Let's not use the yellow and blue colors. Added Thursday, August 31, 2017

Target Market(s)

women and children

Industry/Entity Type

Health And Wellness

Contact Information for Business Card

Business name: Willow Brook Chiropractic & Acupuncture
My name: Lorin Daske
Job title: DC, MSTOM, LAc (NV), CCN

Location 1
Address: 4817 Marlowe Blvd, Suite C-210, Larkfield, TX 75990
Phone: (469) 555-0182
Fax: (972) 555-0137

Location 2
Address: 1936 Belvane Road, Suite 340, Ashmere, TX 75962
Phone: (469) 555-0169
Fax: (972) 555-0137

Email: drlorindaske@mailnest.example
Website: www.drlorindaske.example

Font styles to use
Serif
Sans Serif

Colors

Designer to choose colors to be used in the design.

Requirements
Must have
• distinction between 2 locations.
Nice to have
• Colors preference below is there. But I like to see what you come up with too!

```html
<!DOCTYPE html>
<html lang="en">
<head>
<meta charset="utf-8">
<title>Willow Brook Chiropractic & Acupuncture – Business Card</title>
<link href="https://fonts.googleapis.com/css2?family=Cinzel:wght@600&family=Roboto:wght@400;500&display=swap" rel="stylesheet">
<style>
  :root{
    --bg:#e6e8e6;
    --card:#ffffff;
    --card-back:#f6f7f6;
    --green-dark:#118c3d;
    --green-light:#c3dd8a;
    --teal:#2a6f72;
    --ink:#2b2b2b;
    --text:#3a3a3a;
    --rule:#8a8a8a;
    --accent:#1e9a45;
  }
  *{box-sizing:border-box;margin:0;padding:0}
  html,body{width:1200px;height:900px;overflow:hidden;background:var(--bg)}
  .canvas{width:1200px;height:900px;display:flex;flex-direction:column;align-items:center;justify-content:center;gap:36px}
  .card{width:700px;height:400px;position:relative;overflow:hidden;box-shadow:0 6px 18px rgba(0,0,0,.18)}
  /* front */
  .card-front{background:var(--card)}
  .brand{position:absolute;left:0;right:0;top:95px;display:flex;align-items:center;justify-content:center;gap:22px}
  .brand-dot{width:96px;height:96px;border-radius:50%;border:7px solid var(--teal);flex:none}
  .brand-name{font-family:"Cinzel",serif;font-weight:600;color:var(--teal);line-height:1.15}
  .brand-name .big{display:block;font-size:40px;letter-spacing:1px}
  .brand-name .small{display:block;font-size:15px;letter-spacing:1.5px}
  .band{position:absolute;left:0;right:0;bottom:0;height:62px;display:flex}
  .band-dark{width:38%;background:var(--green-dark)}
  .band-light{width:17%;background:var(--green-light)}
  .band-teal{flex:1;background:var(--teal);display:flex;align-items:center;justify-content:flex-end;padding:0 26px;font-family:"Roboto",sans-serif;font-size:19px;color:#fff;letter-spacing:.5px;white-space:nowrap}
  /* back */
  .card-back{background:var(--card-back)}
  .leaf-field{position:absolute;right:-40px;bottom:-60px;width:470px;height:360px;border-radius:50%;background:radial-gradient(ellipse at center,rgba(150,185,150,.28),rgba(150,185,150,0) 70%)}
  .person{position:absolute;right:38px;top:38px;text-align:right;font-family:"Roboto",sans-serif}
  .person-name{font-size:34px;font-weight:500;color:var(--ink);letter-spacing:1px}
  .person-title{font-size:14px;color:var(--accent);margin-top:2px}
  .back-dot{position:absolute;right:56px;top:150px;width:110px;height:110px;border-radius:50%;border:6px solid var(--teal)}
  .location{position:absolute;left:40px;font-family:"Roboto",sans-serif;color:var(--text)}
  .location-one{top:60px}
  .location-two{top:205px}
  .address{font-size:17px;line-height:1.25;margin-bottom:8px;padding-left:18px}
  .lines{border-left:2px solid var(--rule);padding-left:16px}
  .row{display:flex;align-items:center;gap:12px;font-size:17px;line-height:1.3;white-space:nowrap}
  .row svg{width:16px;height:16px;flex:none}
</style>
</head>
<body>
<main class="canvas">
  <section class="card card-front">
    <div class="brand">
      <span class="brand-dot"></span>
      <div class="brand-name"><span class="big">Willow Brook</span><span class="small">Chiropractic &amp; Acupuncture</span></div>
    </div>
    <div class="band">
      <div class="band-dark"></div>
      <div class="band-light"></div>
      <div class="band-teal">www.drlorindaske.example</div>
    </div>
  </section>

  <section class="card card-back">
    <div class="leaf-field" role="img" aria-label="Faint decorative leaves in soft green"></div>
    <div class="person">
      <div class="person-name">LORIN DASKE</div>
      <div class="person-title">DC, MSTOM, LAc (NV), CCN</div>
    </div>
    <span class="back-dot"></span>

    <div class="location location-one">
      <p class="address">4817 Marlowe Blvd,<br>Suite C-210, Larkfield, TX 75990</p>
      <div class="lines">
        <div class="row"><svg viewBox="0 0 16 16"><path fill="#1e9a45" d="M3 1l3 3-1.5 2a9 9 0 005.5 5.5L12 10l3 3-2 2C7 15 1 9 1 3z"/></svg>(469) 555-0182</div>
        <div class="row"><svg viewBox="0 0 16 16"><rect x="1" y="4" width="14" height="10" fill="#1e9a45"/><path d="M1 4l7 5 7-5" stroke="#fff" fill="none"/></svg>(972) 555-0137</div>
      </div>
    </div>

    <div class="location location-two">
      <p class="address">1936 Belvane Road,<br>Suite 340, Ashmere, TX 75962</p>
      <div class="lines">
        <div class="row"><svg viewBox="0 0 16 16"><path fill="#1e9a45" d="M3 1l3 3-1.5 2a9 9 0 005.5 5.5L12 10l3 3-2 2C7 15 1 9 1 3z"/></svg>(469) 555-0169</div>
        <div class="row"><svg viewBox="0 0 16 16"><rect x="1" y="4" width="14" height="10" fill="#1e9a45"/><path d="M1 4l7 5 7-5" stroke="#fff" fill="none"/></svg>(972) 555-0137</div>
        <div class="row"><svg viewBox="0 0 16 16"><rect x="1" y="3" width="14" height="10" fill="none" stroke="#1e9a45" stroke-width="1.6"/><path d="M1 3l7 6 7-6" stroke="#1e9a45" stroke-width="1.6" fill="none"/></svg>drlorindaske@mailnest.example</div>
        <div class="row"><svg viewBox="0 0 16 16"><circle cx="8" cy="8" r="7" fill="#1e9a45"/><path d="M1 8h14M8 1v14M3 4h10M3 12h10" stroke="#fff" stroke-width=".8" fill="none"/><ellipse cx="8" cy="8" rx="3" ry="7" stroke="#fff" stroke-width=".8" fill="none"/></svg>www.drlorindaske.example</div>
      </div>
    </div>
  </section>
</main>
</body>
</html>
```